Ridgeline Wild Craft DL flyer

I'm looking for a new flyer for my startup business. In Darwin Australia.
Aimed at family's and short stay tourists the "Ridgeline Wild Craft" 4 hr tour will give people a basic understanding of some essential bush survival skills in the Australian Outback.
things covered in this 4 hr tour are
1. Finding water.
2. finding food.
3. Finding/making shelter and fire.
4. Finding your way home.

The tour will pick clients up in an air conditioned purpose build 4WD and take them to a nearby bushland area where they will have the opportunity to catch and harvest some native bushtucker.
They will then be able to find/harvest some water for survival situations.
While we cook our bush tucker they will also learn to find their way home through ancient navigation techniques as well.

Clients will then be dropped back to their accomodation with some fun and vital knowledge of surviving in the Australian outback.
At the end of the tour the group will be able to take home a basic survival kit which they will be able to use through the skills they just gained on the tour.

I'd like a two sided DL size flyer emphasising the following points.
4hr/half day tour
Fun for the family
Free survival kit included.
Eat what you catch
Learn essential survival skills
Provided buy an experienced and passionate bushman.
$150/head including transfers.

I'll provide some pictures for the flyer and any extra content you require.

Target Market(s)

Family's
Short stay tourists

Industry/Entity Type

Tourism

Colors

Designer to choose colors to be used in the design.

Requirements
Must have
• As per brief
Nice to have
• Any extra content and flair designers would like to add
Should not have
• Any images which aren't Australian

```html
<!DOCTYPE html>
<html lang="en">
<head>
<meta charset="utf-8">
<title>Ridgeline Wild Craft – DL Flyer</title>
<link href="https://fonts.googleapis.com/css2?family=Cinzel:wght@400;600;700&family=Quicksand:wght@500&family=Open+Sans:wght@500&display=swap" rel="stylesheet">
<style>
  :root{
    --stage:#58585a;
    --paper:#ffffff;
    --paper-edge:#dcdcdc;
    --blue-deep:#0f4f9c;
    --blue:#1a6fb8;
    --blue-light:#3a9ad9;
    --ink-grey:#555559;
    --white:#ffffff;
  }
  *{margin:0;padding:0;box-sizing:border-box}
  html,body{width:1200px;height:801px;overflow:hidden;background:var(--stage)}
  .stage{position:relative;width:1200px;height:801px;background:var(--stage)}
  .panel{
    position:absolute;top:60px;width:320px;height:680px;overflow:hidden;
    background:linear-gradient(90deg,var(--paper-edge) 0%,var(--paper) 22%,var(--paper) 100%);
    box-shadow:3px 4px 8px rgba(0,0,0,.45);
  }
  .panel--front{left:256px}
  .panel--back{left:624px}
  .panel-art{position:absolute;inset:0;width:320px;height:680px}
  .tour-length{
    position:absolute;left:16px;top:430px;width:290px;text-align:center;
    font-family:"Cinzel",serif;font-weight:600;font-size:31px;color:var(--ink-grey);letter-spacing:.5px;
  }
  .title-rule{position:absolute;left:16px;top:478px;width:288px;height:1.5px;background:var(--ink-grey)}
  .tour-word{
    position:absolute;left:14px;top:468px;width:292px;text-align:center;
    font-family:"Cinzel",serif;font-weight:700;font-size:82px;color:var(--blue);letter-spacing:1px;
  }
  .tagline{
    position:absolute;left:0;top:612px;width:320px;text-align:center;
    font-family:"Cinzel",serif;font-weight:600;font-size:21px;line-height:27px;color:var(--white);
  }
  .highlights{
    position:absolute;left:38px;top:444px;width:270px;list-style:none;
    font-family:"Quicksand",sans-serif;font-weight:500;font-size:15px;line-height:19px;color:var(--white);
  }
  .highlights li{position:relative;padding-left:18px}
  .highlights li::before{content:"";position:absolute;left:0;top:6px;width:7px;height:7px;border-radius:50%;background:var(--white)}
  .contact{
    position:absolute;left:0;top:628px;width:320px;text-align:center;
    font-family:"Open Sans",sans-serif;font-weight:500;font-size:12.5px;line-height:17px;color:var(--white);
  }
</style>
</head>
<body>
<main class="stage">

  <section class="panel panel--front">
    <svg class="panel-art" viewBox="0 0 400 850" preserveAspectRatio="none" aria-hidden="false">
      <defs>
        <linearGradient id="ringBlue" x1="0" y1="0" x2="1" y2="1">
          <stop offset="0" stop-color="#3a9ad9"/><stop offset="1" stop-color="#0f4f9c"/>
        </linearGradient>
        <linearGradient id="bandBlue" x1="0" y1="0" x2="1" y2="0">
          <stop offset="0" stop-color="#0f4f9c"/><stop offset=".6" stop-color="#1a6fb8"/><stop offset="1" stop-color="#3a9ad9"/>
        </linearGradient>
        <linearGradient id="photoGuide" x1="0" y1="0" x2="0" y2="1"><stop offset="0" stop-color="#a9b98f"/><stop offset="1" stop-color="#8d8a78"/></linearGradient>
        <linearGradient id="photoFruit" x1="0" y1="0" x2="1" y2="1"><stop offset="0" stop-color="#7fa6c9"/><stop offset="1" stop-color="#8a6a3a"/></linearGradient>
        <linearGradient id="photoCrab" x1="0" y1="0" x2="0" y2="1"><stop offset="0" stop-color="#6f8a4e"/><stop offset="1" stop-color="#5c4a3c"/></linearGradient>
        <linearGradient id="photoMounds" x1="0" y1="0" x2="0" y2="1"><stop offset="0" stop-color="#8fa6b2"/><stop offset=".5" stop-color="#5f7a3c"/><stop offset="1" stop-color="#9a5a30"/></linearGradient>
      </defs>
      <circle class="ring" cx="235" cy="145" r="185" fill="url(#ringBlue)"/>
      <circle cx="235" cy="145" r="162" fill="#ffffff" opacity=".35"/>
      <circle class="photo" cx="235" cy="145" r="150" fill="url(#photoGuide)" role="img" aria-label="Photo of the bushman guide in a wide-brim hat"/>
      <circle class="ring" cx="80" cy="270" r="88" fill="url(#ringBlue)"/>
      <circle class="photo" cx="80" cy="270" r="74" fill="url(#photoFruit)" role="img" aria-label="Photo of native bush fruit on a branch"/>
      <circle class="ring" cx="255" cy="370" r="103" fill="url(#ringBlue)"/>
      <circle class="photo" cx="255" cy="370" r="86" fill="url(#photoCrab)" role="img" aria-label="Photo of a guest holding a freshly caught mud crab"/>
      <circle class="ring" cx="125" cy="410" r="80" fill="url(#ringBlue)"/>
      <circle class="photo" cx="125" cy="410" r="67" fill="url(#photoMounds)" role="img" aria-label="Photo of termite mounds in outback grassland"/>
      <path d="M0 760 Q200 700 400 760 L400 780 Q200 725 0 780Z" fill="#3a9ad9" opacity=".55"/>
      <path d="M0 780 Q200 728 400 780 L400 850 L0 850Z" fill="url(#bandBlue)"/>
    </svg>
    <h2 class="tour-length">4HR/HALF DAY</h2>
    <div class="title-rule"></div>
    <h1 class="tour-word">TOUR</h1>
    <p class="tagline">FUN<br>FOR THE FAMILY</p>
  </section>

  <section class="panel panel--back">
    <svg class="panel-art" viewBox="0 0 400 850" preserveAspectRatio="none">
      <defs>
        <linearGradient id="ringBlue2" x1="0" y1="0" x2="1" y2="1">
          <stop offset="0" stop-color="#3a9ad9"/><stop offset="1" stop-color="#0f4f9c"/>
        </linearGradient>
        <linearGradient id="bandBlue2" x1="0" y1="0" x2="1" y2="0">
          <stop offset="0" stop-color="#3a9ad9"/><stop offset=".5" stop-color="#1a6fb8"/><stop offset="1" stop-color="#0f4f9c"/>
        </linearGradient>
        <linearGradient id="boxBlue" x1="0" y1="0" x2="0" y2="1">
          <stop offset="0" stop-color="#3a9ad9"/><stop offset="1" stop-color="#0f4f9c"/>
        </linearGradient>
        <linearGradient id="photoCray" x1="0" y1="0" x2="1" y2="1"><stop offset="0" stop-color="#b9a58e"/><stop offset="1" stop-color="#6d7a5e"/></linearGradient>
        <linearGradient id="photoPods" x1="0" y1="0" x2="1" y2="1"><stop offset="0" stop-color="#d8b6a4"/><stop offset="1" stop-color="#7a9a4a"/></linearGradient>
        <linearGradient id="photoPalm" x1="0" y1="0" x2="0" y2="1"><stop offset="0" stop-color="#5f8a4a"/><stop offset="1" stop-color="#a09070"/></linearGradient>
        <linearGradient id="photoNet" x1="0" y1="0" x2="1" y2="1"><stop offset="0" stop-color="#3f6a3a"/><stop offset="1" stop-color="#c9d1d6"/></linearGradient>
      </defs>
      <circle cx="165" cy="145" r="185" fill="url(#ringBlue2)"/>
      <circle cx="165" cy="145" r="162" fill="#ffffff" opacity=".35"/>
      <circle cx="165" cy="145" r="150" fill="url(#photoCray)" role="img" aria-label="Photo of a freshwater crayfish held in open hands"/>
      <circle cx="320" cy="275" r="82" fill="url(#ringBlue2)"/>
      <circle cx="320" cy="275" r="68" fill="url(#photoPods)" role="img" aria-label="Photo of hairy green bush seed pods in a palm"/>
      <circle cx="140" cy="370" r="104" fill="url(#ringBlue2)"/>
      <circle cx="140" cy="370" r="88" fill="url(#photoPalm)" role="img" aria-label="Photo of a pandanus palm in the bush"/>
      <circle cx="280" cy="415" r="74" fill="url(#ringBlue2)"/>
      <circle cx="280" cy="415" r="61" fill="url(#photoNet)" role="img" aria-label="Photo of a plastic sheet water collector on green foliage"/>
      <path d="M25 538 Q200 560 375 535 Q390 628 372 722 Q200 700 30 722 Q12 628 25 538Z" fill="url(#boxBlue)"/>
      <path d="M0 760 Q200 700 400 760 L400 780 Q200 725 0 780Z" fill="#3a9ad9" opacity=".55"/>
      <path d="M0 780 Q200 728 400 780 L400 850 L0 850Z" fill="url(#bandBlue2)"/>
    </svg>
    <ul class="highlights">
      <li>Free survival kit included.</li>
      <li>Eat what you catch</li>
      <li>Learn essential survival skills</li>
      <li>Provided buy an experienced and passionate bushman.</li>
      <li>$150/head including transfers.</li>
    </ul>
    <p class="contact">Contat us:<br>+00 000 0000 | Email:ridgelinetour@example.com</p>
  </section>

</main>
</body>
</html>
```